Design a menu for health restaurant

A health food restaurant in Los Angeles is seeking menu design. Our foods are made from scratch using whole ingredients.
Name: Grove Pantry
Address: 1000 E 60th StLos Angeles, CA 90347
Website: www.GrovePantry-example.com
We are looking for a clean and simple menu. Brand colors are white/tan, green and orange.

Please see attached excel with menu items and logo. We do not yet have prices.

Colors
f78f20
9bcb3c
ffffff
fff3d1

Requirements
Must have
• Easy to read.
Trifold menu design (front and back).
VEGAN, VEGETARIAN, GLUTEN FREE, CONTAINS NUTS symbols.
Logo.
Nice to have
• Incorporate brand colors, but still be easy to read.
We would like to use the Belco font (attached) if it works. If not we are open to a similar font that is easy to read.

Please see attached images.
We like the images and headers of OPTION 1. Would like something similar in trifold format.
We like the clean fonts of OPTION 2.

```html
<!DOCTYPE html>
<html lang="en">
<head>
<meta charset="utf-8">
<title>Grove Pantry Menu</title>
<link rel="stylesheet" href="https://fonts.googleapis.com/css2?family=Barlow:ital,wght@0,400;0,500;1,300&family=Zilla+Slab:ital,wght@0,400;1,700&display=swap">
<style>
  :root{
    --green:#9bcb3c;
    --orange:#f26b21;
    --paper:#e3e2dd;
    --ink:#1f1f1f;
    --muted:#6a6a6a;
    --white:#ffffff;
    --rule:#8d8d8d;
  }
  html,body{margin:0;padding:0;overflow:hidden;background:var(--white);}
  .menu{position:relative;width:1200px;height:933px;overflow:hidden;background:var(--white);font-family:"Barlow",sans-serif;color:var(--ink);}
  .sheet{position:absolute;left:14px;top:14px;width:1172px;height:904px;background:var(--paper);}
  .section-head{position:absolute;height:70px;}
  .section-head h2{margin:0;position:absolute;left:17px;top:15px;font-family:"Zilla Slab",serif;font-style:italic;font-weight:700;font-size:33px;color:var(--white);letter-spacing:.5px;line-height:1;}
  .section-head .band{position:absolute;left:0;right:0;bottom:0;height:13px;}
  .head-green{background:var(--green);}
  .head-green .band{background:#d9ebb4;}
  .head-orange{background:var(--orange);}
  .head-orange .band{background:#f8c09f;}
  .photo{position:absolute;}
  .item{position:absolute;}
  .item h3{margin:0;font-weight:500;font-size:12px;line-height:14px;display:flex;align-items:center;gap:3px;}
  .item p{margin:2px 0 0;font-style:italic;font-weight:300;font-size:9.3px;line-height:11.6px;color:var(--muted);}
  .price{position:absolute;right:0;top:0;font-weight:500;font-size:11.5px;line-height:14px;}
  .badge{display:inline-flex;align-items:center;justify-content:center;font-size:4.5px;font-weight:500;color:#555;border:0.7px solid #777;box-sizing:border-box;margin-left:2px;}
  .b-veg{width:7px;height:7px;transform:rotate(45deg);margin:0 3px;}
  .b-veg span{transform:rotate(-45deg);}
  .b-gf{width:9px;height:9px;border-radius:50%;}
  .b-vegan{width:9px;height:8px;}
  .b-nuts{width:11px;height:8px;border-radius:4px;}
  .legend{position:absolute;left:14px;top:866px;width:1172px;height:26px;border-top:2px solid var(--rule);border-bottom:2px solid var(--rule);}
  .legend-entry{position:absolute;top:5px;display:flex;align-items:center;gap:6px;font-family:"Zilla Slab",serif;font-size:11.5px;letter-spacing:.3px;color:var(--ink);}
  .legend-entry .badge{font-size:6px;}
  .legend-entry .b-veg{width:10px;height:10px;}
  .legend-entry .b-gf{width:14px;height:14px;}
  .legend-entry .b-vegan{width:14px;height:13px;}
  .legend-entry .b-nuts{width:17px;height:12px;border-radius:6px;}
</style>
</head>
<body>
<div class="menu">
  <div class="sheet"></div>

  <!-- Breakfast -->
  <div class="section-head head-green" style="left:14px;top:14px;width:383px;">
    <h2>BREAKFAST</h2><div class="band" role="img" aria-label="Striped band"></div>
  </div>
  <div class="photo" role="img" aria-label="Avocado toast with cherry tomatoes and chickpeas" style="left:32px;top:100px;width:347px;height:83px;background:linear-gradient(90deg,#e9e9e6,#a7c45c 30%,#6b4a2e 50%,#9cc155 70%,#e6e6e3);"></div>

  <div class="item" style="left:31px;top:193px;width:348px;"><h3>Pastries<i class="badge b-veg"><span>V</span></i></h3><span class="price">11.99</span><p>Croissant (regular, almond, chocolate)<br>Blueberry Muffin<br>Superseed Cookie</p></div>
  <div class="item" style="left:31px;top:248px;width:348px;"><h3>Parfait<i class="badge b-veg"><span>V</span></i></h3><span class="price">11.99</span><p>Fresh strawberries and blueberries on yogurT<br>and muesli and topped with honey drizzle.</p></div>
  <div class="item" style="left:31px;top:290px;width:348px;"><h3>Avocado Super Toast<i class="badge b-vegan">V+</i></h3><span class="price">11.99</span><p>Avocado Mash, Tomato, Basil, Ground Flax, Hemp Seed<br>Chickpeas, and Moringa Powder on Whole Wheat Bread.</p></div>
  <div class="item" style="left:31px;top:333px;width:348px;"><h3>Brunch Burger</h3><span class="price">11.99</span><p>House seasoned beef burger topped with an over<br>medium egg, red leaf lettuce, tomato, housemade<br>pickles and Pantry Sauce on a bun.</p></div>
  <div class="item" style="left:31px;top:387px;width:348px;"><h3>Breakfast Sammy<i class="badge b-vegan">V+</i></h3><span class="price">11.99</span><p>Your choice of over medium egg or tofu steak with guacamole,<br>tomato, and Pantry sauce on an English muffin.</p></div>
  <div class="item" style="left:31px;top:430px;width:348px;"><h3>AM Burrito<i class="badge b-veg"><span>V</span></i></h3><span class="price">11.99</span><p>Scrambled eggs, onion, red bell pepper, black beans,<br>housemade salsa, yogurt, and pepper jack cheese in a tortilla.</p></div>

  <!-- Smoothies -->
  <div class="section-head head-orange" style="left:14px;top:494px;width:383px;">
    <h2>SMOOTHIES</h2><div class="band" role="img" aria-label="Striped band"></div>
  </div>
  <div class="item" style="left:31px;top:585px;width:348px;"><h3>Green Machine Smoothie<i class="badge b-vegan">V+</i><i class="badge b-gf">GF</i><i class="badge b-nuts">N+</i></h3><span class="price">11.99</span><p>Romaine, spinach, banana, mango, pineapple, flaxmilk,<br>spirulina, almond butter.</p></div>
  <div class="item" style="left:31px;top:628px;width:348px;"><h3>Acai Smoothie<i class="badge b-vegan">V+</i><i class="badge b-gf">GF</i><i class="badge b-nuts">N+</i></h3><span class="price">11.99</span><p>Acai, blueberries, banana, pineapple, Macqui berry, flaxmilk,<br>almond butter</p></div>
  <div class="item" style="left:31px;top:673px;width:348px;"><h3>Mango Smoothies<i class="badge b-gf">GF</i><i class="badge b-nuts">N+</i></h3><span class="price">11.99</span><p>Mango, flaxmilk, banan, hemp seeds</p></div>
  <div class="photo" role="img" aria-label="Glass of mango smoothie" style="left:82px;top:707px;width:234px;height:133px;background:radial-gradient(ellipse at 50% 45%,#f7b928 0%,#f5c443 45%,#dedcd8 75%);"></div>

  <!-- Bowls -->
  <div class="section-head head-orange" style="left:408px;top:14px;width:384px;">
    <h2>BOWLS</h2><div class="band" role="img" aria-label="Striped band"></div>
  </div>
  <div class="item" style="left:425px;top:100px;width:348px;"><h3>Southwest Bowl<i class="badge b-gf">GF</i><i class="badge b-nuts">N+</i></h3><span class="price">11.99</span><p>Your choice of protein with corn, black beans, red onions,<br>almonds and avocado over quinoa with lime hot sauce.</p></div>
  <div class="item" style="left:425px;top:143px;width:348px;"><h3>Chimi Bowl<i class="badge b-gf">GF</i></h3><span class="price">11.99</span><p>Your choice of protein with red bell pepper, mushrooms,<br>zucchini, squash, onion, cherry tomatoes and fresh herb<br>chimichurri on wild and brown rice.</p></div>
  <div class="item" style="left:425px;top:198px;width:348px;"><h3>Soba Noodle Bowl</h3><span class="price">11.99</span><p>Your choice of protein with red bell pepper, mushrooms,<br>zucchini, squash, onion, cherry tomatoes and fresh herb<br>chimichurri on wild and brown rice.</p></div>
  <div class="item" style="left:425px;top:252px;width:348px;"><h3>Hollywood Bow<i class="badge b-gf">GF</i></h3><span class="price">11.99</span><p>Your choice of protein with broccoli, roasted corn, cherry<br>tomatoes, basil, pepitas, flax seeds and lemon juice on<br>wild and brown rice.</p></div>
  <div class="item" style="left:425px;top:307px;width:348px;"><h3>Pantry Bowl<i class="badge b-gf">GF</i></h3><span class="price">11.99</span><p>Your choice of protein with roasted chickpeas and<br>cauliflower, zesty fennel salad and citrus yogurt.</p></div>
  <div class="item" style="left:425px;top:352px;width:348px;"><h3>Buddha Bowl</h3><span class="price">11.99</span><p>Your choice of protein with roasted chickpeas and<br>cauliflower, zesty &nbsp;fennel saladand citrus yogurt.</p></div>
  <div class="item" style="left:425px;top:396px;width:348px;"><h3>Chili Rice Bowl<i class="badge b-gf">GF</i></h3><span class="price">11.99</span><p>Chicken, onions, bell peppers, jalapeños, black &amp; kidney<br>beans, and tomato over brown rice.</p></div>
  <div class="photo" role="img" aria-label="Grilled chicken bowl with peppers and corn" style="left:425px;top:446px;width:346px;height:90px;background:linear-gradient(90deg,#e6e6e2,#5b7d34 18%,#d9a979 45%,#e2c39c 65%,#6c8c3a 85%,#e6e6e2);"></div>

  <!-- Soups -->
  <div class="section-head head-green" style="left:404px;top:553px;width:384px;">
    <h2>SOUPS</h2><div class="band" role="img" aria-label="Striped band"></div>
  </div>
  <div class="item" style="left:425px;top:636px;width:348px;"><h3>Green Machine Smoothie<i class="badge b-vegan">V+</i><i class="badge b-gf">GF</i><i class="badge b-nuts">N+</i></h3><span class="price">11.99</span><p>Romaine, spinach, banana, mango, pineapple, flaxmilk,<br>spirulina, almond butter.</p></div>
  <div class="item" style="left:425px;top:681px;width:348px;"><h3>Acai Smoothie<i class="badge b-vegan">V+</i><i class="badge b-gf">GF</i><i class="badge b-nuts">N+</i></h3><span class="price">11.99</span><p>Acai, blueberries, banana, pineapple, Macqui berry,<br>flaxmilk, almond butter</p></div>
  <div class="item" style="left:424px;top:725px;width:349px;"><h3>Mango Smoothie<i class="badge b-gf">GF</i><i class="badge b-nuts">N+</i></h3><span class="price">11.99</span><p>Mango, flaxmilk, banan, hemp seeds</p></div>
  <div class="photo" role="img" aria-label="Bowl of squash soup with herbs" style="left:424px;top:767px;width:349px;height:72px;background:radial-gradient(ellipse at 50% 40%,#d38f1e 0%,#c8841c 55%,#e4e3df 85%);"></div>

  <!-- Wraps -->
  <div class="section-head head-green" style="left:802px;top:14px;width:384px;">
    <h2>WRAPS</h2><div class="band" role="img" aria-label="Striped band"></div>
  </div>
  <div class="item" style="left:817px;top:100px;width:351px;"><h3>Rancher's Wrap</h3><span class="price">11.99</span><p>Tomato, red onion, hard boiled egg, avocado, feta cheese, microgreens,<br>romaine, grilled chicken and Ranch dressing in a grilled wrap.</p></div>
  <div class="item" style="left:817px;top:144px;width:351px;"><h3>Vegan Tuna Wrap</h3><span class="price">11.99</span><p>Vegan tuna, romaine, avocado, celery, shallot, and oregano with<br>Herbalicious Sauce in a whole grain wrap.</p></div>
  <div class="item" style="left:817px;top:186px;width:351px;"><h3>Vegetarian Wrap</h3><span class="price">11.99</span><p>Roasted chickpeas, romaine, avocado, red bell pepper, shaved carrots,<br>cucumber, spinach, basil, black beans and feta with lemon-hummus in<br>a sprouted 7-grain wrap.</p></div>
  <div class="photo" role="img" aria-label="Vegan tuna wrap cut in half" style="left:833px;top:244px;width:322px;height:98px;background:linear-gradient(90deg,#f0efe9,#8fb35a 20%,#c9a58e 45%,#d9462c 65%,#7fae4d 80%,#f0efe9);"></div>

  <!-- Salad -->
  <div class="section-head head-orange" style="left:802px;top:353px;width:384px;">
    <h2>SALAD</h2><div class="band" role="img" aria-label="Striped band"></div>
  </div>
  <div class="photo" role="img" aria-label="Grilled chicken salad with roasted peppers" style="left:818px;top:445px;width:348px;height:111px;background:radial-gradient(ellipse at 50% 50%,#d58f3f 0%,#5f8a36 55%,#e2e2de 90%);"></div>
  <div class="item" style="left:819px;top:574px;width:349px;"><h3>Avocado, Golden Beet,</h3><h3>and Cranberry Salad<i class="badge b-veg"><span>V</span></i><i class="badge b-gf">GF</i></h3><span class="price" style="top:14px;">11.99</span><p>Gold beets, avocado, dried cranberries, watermelon radish,<br>red kale, romaine, mixed greens, and pepitas served with<br>Golden Buddha dressing.</p></div>
  <div class="item" style="left:819px;top:645px;width:349px;"><h3>Burrata Salad<i class="badge b-veg"><span>V</span></i><i class="badge b-gf">GF</i></h3><span class="price">11.99</span><p>Tomato, melon, shredded basil, balsamic glaze, fresh<br>cracked pepper, and olive oil with burrata.</p></div>
  <div class="item" style="left:817px;top:687px;width:351px;"><h3>Mediterranean Salad<i class="badge b-veg"><span>V</span></i><i class="badge b-gf">GF</i></h3><span class="price">11.99</span><p>Cucumbers, Kalamata olives, cherry tomatoes, parsley,<br>tricolor quinoa, hard-boiled egg, and hummus on<br>mixed greens, romaine, and redcabbage with lemon-olive oil dressing.</p></div>
  <div class="item" style="left:817px;top:744px;width:351px;"><h3>Vegan Chef Salad<i class="badge b-vegan">V+</i><i class="badge b-gf">GF</i><i class="badge b-nuts">N+</i></h3><span class="price">11.99</span><p>Roasted potatoes and carrots, chickpeas, avocado,<br>microgreens and walnuts on mixed greens,<br>romaine, and red kale with vegan ranch.</p></div>
  <div class="item" style="left:819px;top:801px;width:349px;"><h3>Rancher's Salad<i class="badge b-veg"><span>V</span></i><i class="badge b-gf">GF</i></h3><span class="price">11.99</span><p>Tomato, red onion, hard boiled egg, avocado, feta cheese,<br>microgreens, and grilled chicken on romaine with Ranch dressing.</p></div>

  <!-- Legend -->
  <div class="legend">
    <div class="legend-entry" style="left:56px;"><i class="badge b-veg"><span>V</span></i>VEGETARIAN</div>
    <div class="legend-entry" style="left:369px;"><i class="badge b-gf">GF</i>GLUTEN FREE</div>
    <div class="legend-entry" style="left:681px;"><i class="badge b-vegan">V+</i>VEGAN</div>
    <div class="legend-entry" style="left:987px;"><i class="badge b-nuts">N+</i>CONTAINS NUTS</div>
  </div>
</div>
</body>
</html>
```